Business Cards for a Junk Removal Company

Hello,
We are looking to have business cards designed that are simple, bold, easy to read, and right to the point. Please see the attachments for our logo files. We want the card to be yellow on both sides ( Color code Yellow: #FFE01B). The logo text font is (Rockstar Extra Bold) and this is also in the files attached. Please make the text black for the logo. On the back side of the card, you can use white and black for text. Thank you in advance for your hard work!

Front of card-
Harbor Haul Away (logo)
Back of card-
Harbor Haul Away
Donate - Recycle - Dispose
555-271-8093
www.harborhaulaway.example
info@harborhaulaway.example

Industry/Entity Type

Junk removal

Contact Information for Business Card

FRONT OF CARD- Harbor Haul Away (logo) BACK OF CARD- Harbor Haul Away Donate - Recycle - Dispose 555-271-8093 www.harborhaulaway.example info@harborhaulaway.example

Font styles to use
Other font styles liked:
• Rockstar Extra Bold

Colors
FFF300
FFF600
FEFA6F
FFFEC7
FFFEE8

Requirements
Must have
• Must have color code Yellow: #FFE01B for the background of front and back of the card

```html
<!DOCTYPE html>
<html lang="en">
<head>
<meta charset="utf-8">
<title>Harbor Haul Away — Business Cards</title>
<link href="https://fonts.googleapis.com/css2?family=Anton&family=Roboto:wght@500&display=swap" rel="stylesheet">
<style>
  :root {
    --backdrop: #2a2a2a;
    --card-yellow: #dfc441;
    --card-yellow-light: #e4c945;
    --ink: #111111;
    --band: #232323;
    --band-text: #dfc441;
  }
  * { box-sizing: border-box; margin: 0; padding: 0; }
  html, body {
    width: 1200px;
    height: 1138px;
    overflow: hidden;
    background: var(--backdrop);
  }
  .sheet {
    position: relative;
    width: 1200px;
    height: 1138px;
  }
  .card {
    position: absolute;
    left: 275px;
    width: 620px;
    height: 375px;
    border-radius: 16px;
    background: linear-gradient(160deg, var(--card-yellow-light), var(--card-yellow));
    overflow: hidden;
  }
  .card--front { top: 186px; }
  .card--back { top: 608px; }

  .brand-name {
    font-family: "Anton", "Impact", sans-serif;
    color: var(--ink);
    text-transform: uppercase;
    text-align: center;
    white-space: nowrap;
    letter-spacing: 1px;
    line-height: 1;
  }
  .card--front .brand-name {
    position: absolute;
    left: 0; right: 0;
    top: 150px;
    font-size: 64px;
  }
  .card--back .brand-name {
    position: absolute;
    left: 0; right: 0;
    top: 74px;
    font-size: 60px;
  }

  .call-band {
    position: absolute;
    left: 0; right: 0;
    top: 216px;
    height: 56px;
    background: var(--band);
    display: flex;
    align-items: center;
    justify-content: center;
    gap: 12px;
    font-family: "Anton", "Impact", sans-serif;
    color: var(--band-text);
    text-transform: uppercase;
  }
  .call-band__label { font-size: 22px; letter-spacing: 0.3px; }
  .call-band__number { font-size: 32px; letter-spacing: 0.5px; }

  .contact-row {
    position: absolute;
    left: 0; right: 0;
    top: 286px;
    display: flex;
    justify-content: center;
    align-items: center;
    gap: 14px;
    font-family: "Roboto", sans-serif;
    font-weight: 500;
    font-size: 15px;
    color: var(--ink);
  }
  .contact-item { display: flex; align-items: center; gap: 10px; }
  .contact-item svg { width: 14px; height: 14px; }

  .tagline {
    position: absolute;
    left: 0; right: 0;
    top: 334px;
    text-align: center;
    font-family: "Anton", "Impact", sans-serif;
    font-size: 18px;
    color: var(--ink);
    text-transform: uppercase;
    letter-spacing: 0.3px;
  }
</style>
</head>
<body>
<main class="sheet">
  <section class="card card--front" aria-label="Card front">
    <h1 class="brand-name">Harbor Haul Away</h1>
  </section>

  <section class="card card--back" aria-label="Card back">
    <h2 class="brand-name">Harbor Haul Away</h2>

    <div class="call-band">
      <span class="call-band__label">Call us anytime:</span>
      <span class="call-band__number">555-271-8093</span>
    </div>

    <div class="contact-row">
      <span class="contact-item">
        <svg viewBox="0 0 14 14" aria-hidden="true">
          <rect x="1" y="3" width="12" height="8" fill="#111"/>
          <path d="M1 3 L7 8 L13 3" stroke="#dfc441" stroke-width="1.2" fill="none"/>
        </svg>
        info@harborhaulaway.example
      </span>
      <span class="contact-item">
        <svg viewBox="0 0 14 14" aria-hidden="true">
          <circle cx="7" cy="7" r="5.8" fill="none" stroke="#111" stroke-width="1.3"/>
          <ellipse cx="7" cy="7" rx="2.5" ry="5.8" fill="none" stroke="#111" stroke-width="1.1"/>
          <line x1="1.2" y1="7" x2="12.8" y2="7" stroke="#111" stroke-width="1.1"/>
        </svg>
        www.harborhaulaway.example
      </span>
    </div>

    <p class="tagline">Donate - Recycle - Dispose</p>
  </section>
</main>
</body>
</html>
```